New Corporate Business Card - Velmorabelle

What we need:
We need a new corporate business card.
We want a new template that we can change by ourself.
We want business card modern and minimalist but that looks professional.
We will print it in 300 gr soft-touch.
Why not a white side with the logo and a red/grey side with the content?
Why not a grey side and a red side like our logo?
I am sure that you have better idea than ours that's the reason we come here.

Who we are:
We are a private label company in cosmetics based in Switzerland. We work in BtoB. We make skin care products for other brands.

Target Market(s)

B to B - Worldwide - any gender

Industry/Entity Type

Cosmetics

Contact Information for Business Card

Side 1:
Logo
Your Swiss Private Label Manufacturer or www.velmorabelle.ch

Side 2:
Name and surname (Example: Lucien Marchetaz)
Job Description (General Manager)
Telephone (+41 32 918 64 00)
Direct (+41 32 918 64 64)
Email (lucien.marchetaz@velmorabelle.ch)
Chemin des Prés-Fleuris 14, 2000 Neuchâtel, Switzerland
www.velmorabelle.ch

Font styles to use
Serif
Sans Serif

Requirements
Must have
• You can use 4 colors: white, red, grey and/or black .
Should not have
• Too much colors, too much things. We want it simple!

```html
<!DOCTYPE html>
<html lang="en">
<head>
<meta charset="utf-8">
<title>Velmorabelle – Business Card</title>
<link rel="stylesheet" href="https://fonts.googleapis.com/css2?family=Lato:wght@400;700&display=swap">
<style>
  :root {
    --stage: #232323;
    --brand-red: #e01e1a;
    --brand-grey: #a7a8aa;
    --text-grey: #8c8c8c;
    --paper: #ffffff;
  }
  * { margin: 0; padding: 0; box-sizing: border-box; }
  html, body {
    width: 1200px; height: 930px; overflow: hidden;
    background: var(--stage);
    font-family: "Lato", Arial, sans-serif;
  }
  .canvas { position: relative; width: 1200px; height: 930px; }

  .card {
    position: absolute;
    width: 560px; height: 320px;
    box-shadow: 0 10px 30px rgba(0,0,0,.45);
  }
  .card--front { left: 110px; top: 110px; background: var(--brand-red); }
  .card--back  { left: 530px; top: 500px; background: var(--paper); }

  .brand {
    position: absolute;
    display: flex; align-items: center; gap: 14px;
  }
  .card--front .brand {
    left: 50%; top: 50%; transform: translate(-50%, -50%);
  }
  .brand__mark { width: 22px; height: 22px; }
  .brand__name {
    font-weight: 400; font-size: 34px; letter-spacing: 6px;
  }
  .card--front .brand__mark { background: var(--brand-grey); }
  .card--front .brand__name { color: var(--paper); }

  .card--back .brand { left: 36px; top: 140px; }
  .card--back .brand__mark { background: var(--brand-red); width: 16px; height: 16px; }
  .card--back .brand__name { color: var(--brand-red); font-size: 22px; letter-spacing: 3px; }

  .contact {
    position: absolute; left: 292px; top: 70px;
    color: var(--text-grey); font-size: 12px; line-height: 1.35;
  }
  .contact__name { color: var(--brand-red); font-weight: 700; font-size: 20px; line-height: 1.1; }
  .contact__role { font-size: 12.5px; margin-bottom: 12px; }
  .contact__address { margin-bottom: 12px; font-size: 12.5px; }
  .contact__list { list-style: none; }
  .contact__item { display: flex; align-items: center; gap: 7px; }
  .contact__icon { width: 10px; height: 10px; flex: none; fill: none; stroke: var(--brand-red); stroke-width: 1.6; }
</style>
</head>
<body>
<main class="canvas">

  <section class="card card--front" aria-label="Card front">
    <div class="brand">
      <span class="brand__mark"></span>
      <span class="brand__name">Velmorabelle</span>
    </div>
  </section>

  <section class="card card--back" aria-label="Card back">
    <div class="brand">
      <span class="brand__mark"></span>
      <span class="brand__name">Velmorabelle</span>
    </div>

    <div class="contact">
      <p class="contact__name">Lucien Marchetaz</p>
      <p class="contact__role">General Manager</p>
      <p class="contact__address">Chemin des Prés-Fleuris 14,<br>2000 Neuchâtel, Switzerland</p>
      <ul class="contact__list">
        <li class="contact__item">
          <svg class="contact__icon" viewBox="0 0 10 10"><path d="M2 1 L4 3 L3 4.5 Q4.5 6.5 5.5 7 L7 6 L9 8 L7.5 9.3 Q3 8 .8 2.5 Z"/></svg>
          (+41 32 918 64 00)
        </li>
        <li class="contact__item">
          <svg class="contact__icon" viewBox="0 0 10 10"><rect x="2.5" y=".8" width="5" height="8.4" rx="1"/><line x1="4.3" y1="7.5" x2="5.7" y2="7.5"/></svg>
          (+41 32 918 64 64)
        </li>
        <li class="contact__item">
          <svg class="contact__icon" viewBox="0 0 10 10"><circle cx="5" cy="5" r="4"/><ellipse cx="5" cy="5" rx="1.8" ry="4"/><line x1="1" y1="5" x2="9" y2="5"/></svg>
          www.velmorabelle.ch
        </li>
        <li class="contact__item">
          <svg class="contact__icon" viewBox="0 0 10 10"><rect x=".8" y="2" width="8.4" height="6"/><path d="M.8 2 L5 5.5 L9.2 2"/></svg>
          lucien.marchetaz@velmorabelle.ch
        </li>
      </ul>
    </div>
  </section>

</main>
</body>
</html>
```